Business Cards for an 'affordable luxury' inner city home builder in Calgary.

We need a business card design that emulates the progressive, innovative, culture of our company and the modern style of our homes. Use our website www.velmarcrest-ab.com as a reference for the product we build.

Our company builds homes in the inner city space of Calgary, Alberta. We build affordable luxury.

Target Market(s)

Young professional Families

Contact Information for Business Card

Try to maintain consistency with the logo font and the card font.

Requirements
Must have
• The details must include: Name, education, title, phone number, website and email (Address is not as important)
• The design must be uniques (like our logo), elegant, sophisticated and modern.

```html
<!DOCTYPE html>
<html lang="en">
<head>
<meta charset="utf-8">
<title>Velmarcrest Homes Ltd — Business Cards</title>
<link rel="stylesheet" href="https://fonts.googleapis.com/css2?family=Montserrat:wght@600&family=Fira+Sans:wght@400;600&display=swap">
<style>
  :root {
    --backdrop: #1f2327;
    --ink-dark: #2a2a2a;
    --ink-mid: #6b6b6b;
    --paper: #ffffff;
    --band: #2f2f2f;
    --rule: #8a8a8a;
  }
  * { box-sizing: border-box; margin: 0; padding: 0; }
  html, body { width: 1200px; height: 900px; overflow: hidden; }
  body {
    background: var(--backdrop);
    font-family: "Fira Sans", sans-serif;
  }
  .canvas {
    position: relative;
    width: 1200px;
    height: 900px;
  }
  .card {
    position: absolute;
    top: 300px;
    width: 525px;
    height: 300px;
    overflow: hidden;
  }
  .card--front { left: 50px; background: var(--paper); }
  .card--back  { left: 625px; background: var(--band); }

  /* front */
  .front__stripe-top {
    position: absolute; left: 0; top: 0; width: 100%; height: 14px;
    background: var(--band);
  }
  .front__band-bottom {
    position: absolute; left: 0; bottom: 0; width: 100%; height: 44px;
    background: var(--band);
    color: var(--paper);
    font-size: 15px;
    display: flex; align-items: center;
    padding-left: 42px;
  }
  .front__brand {
    position: absolute; left: 150px; top: 44px;
    display: flex; align-items: center; gap: 16px;
  }
  .brand-square {
    width: 30px; height: 30px;
    border: 3px solid var(--ink-dark);
  }
  .brand-name {
    font-family: "Montserrat", sans-serif;
    font-weight: 600;
    font-size: 19px;
    line-height: 1.05;
    letter-spacing: 0.5px;
    color: var(--ink-dark);
    text-transform: uppercase;
  }
  .front__person {
    position: absolute; left: 42px; top: 150px; width: 190px;
    text-align: right;
  }
  .person-name {
    font-weight: 600; font-size: 20px; color: var(--ink-mid);
    letter-spacing: 0.5px;
  }
  .person-title { font-size: 15px; color: var(--ink-mid); margin-top: 2px; }
  .front__divider {
    position: absolute; left: 252px; top: 138px; width: 1.5px; height: 80px;
    background: var(--rule);
  }
  .front__contacts {
    position: absolute; left: 272px; top: 144px;
    list-style: none;
    font-size: 14.5px; color: var(--ink-dark);
  }
  .front__contacts li { display: flex; align-items: center; gap: 8px; height: 23px; }
  .front__contacts svg { width: 12px; height: 12px; fill: var(--ink-mid); flex: none; }

  /* back */
  .back__name {
    position: absolute; left: 60px; top: 40px;
    font-family: "Montserrat", sans-serif;
    font-weight: 600;
    font-size: 26px;
    line-height: 1.05;
    letter-spacing: 1px;
    color: var(--paper);
    text-transform: uppercase;
  }
  .back__web {
    position: absolute; left: 60px; top: 168px;
    font-size: 15px; color: var(--paper);
  }
  .back__mark {
    position: absolute; left: 330px; top: 140px;
    width: 190px; height: 190px;
    border: 14px solid var(--paper);
  }
</style>
</head>
<body>
<main class="canvas">
  <section class="card card--front" aria-label="Business card front">
    <div class="front__stripe-top"></div>
    <div class="front__brand">
      <span class="brand-square" aria-hidden="true"></span>
      <span class="brand-name">Velmarcrest<br>Homes Ltd</span>
    </div>
    <div class="front__person">
      <p class="person-name">YOUR NAME</p>
      <p class="person-title">Your Title</p>
    </div>
    <div class="front__divider"></div>
    <ul class="front__contacts">
      <li>
        <svg viewBox="0 0 24 24" aria-hidden="true"><path d="M6.6 10.8a15 15 0 0 0 6.6 6.6l2.2-2.2a1 1 0 0 1 1-.25 11.4 11.4 0 0 0 3.6.57 1 1 0 0 1 1 1V20a1 1 0 0 1-1 1A17 17 0 0 1 3 4a1 1 0 0 1 1-1h3.5a1 1 0 0 1 1 1c0 1.25.2 2.45.57 3.57a1 1 0 0 1-.25 1z"/></svg>
        403-555-0148
      </li>
      <li>
        <svg viewBox="0 0 24 24" aria-hidden="true"><path d="M2 5h20v14H2z M2 5l10 8 10-8" fill="none" stroke="#6b6b6b" stroke-width="2"/></svg>
        projects@velmarcrest-ab.com
      </li>
      <li>
        <svg viewBox="0 0 24 24" aria-hidden="true"><circle cx="12" cy="12" r="10"/></svg>
        www.velmarcrest-ab.com
      </li>
    </ul>
    <div class="front__band-bottom">418 Maple Ave NE, Calgary, AB</div>
  </section>

  <section class="card card--back" aria-label="Business card back">
    <p class="back__name">Velmarcrest<br>Homes Ltd</p>
    <p class="back__web">www.velmarcrest-ab.com</p>
    <div class="back__mark" role="img" aria-label="Large brand mark area"></div>
  </section>
</main>
</body>
</html>
```